new CPAP Nest flyer

Redesign our flyer completely. A copy of our current flyers are attached (which are being combined into 1). Use anything from these that u want.
It's given to patients with a whole lot of flyers from our competitors - so needs to stand out
Essential elements are:
1. Text: $99 CPAP Trial (prominent - this is the main point of the flyer)
- Our all inclusive 4 week CPAP or APAP trial includes everything you need to get started for just $99. Plus we'll refund your trial fee when you're ready to buy your own machine.
2. Text: Proudly Independent! (keep this separate from themain promotion.
- Many CPAP clinics in Victoria are now owned by one or other of the big CPAP manufacturers; while many others only stock one brand. We stock all the leading brands and offer genuinely independent advice and friendly service.
3. Text: Call us for an appointment
- Ashburton (03) 5550 1842 5/317 Lantern Street (suburb and phone prominent)
- Brighton (03) 5550 2967 27b Penrose Grove (suburb and phone prominent)
- Kew East (03) 5550 3175 2816 Tamsin Road (suburb and phone prominent)
4. Our logo - attached
5. small supplier logos grouped together - vordane, kylofen, brandle&voss - attached
6. images for background / filler - kylofen machine, bvh machine - attached, must use at least one of kylofen pics
Call

```html
<!DOCTYPE html>
<html lang="en">
<head>
<meta charset="utf-8">
<title>CPAP Nest – $99 CPAP Trial Flyer</title>
<link rel="stylesheet" href="https://fonts.googleapis.com/css2?family=Open+Sans:wght@400;600;700;800&display=swap">
<style>
  :root {
    --stage: #e6e6e6;
    --paper: #ffffff;
    --green: #7cb518;
    --blue: #5bc4ee;
    --blue-light: #cdeefa;
    --grey-text: #4a4a4a;
    --dark-text: #222222;
    --band: #ececec;
    --navy: #1f3f8f;
  }
  * { box-sizing: border-box; margin: 0; padding: 0; }
  html, body { width: 1200px; height: 960px; overflow: hidden; }
  body {
    background: var(--stage);
    font-family: "Open Sans", Arial, sans-serif;
    position: relative;
  }
  .flyer {
    position: absolute;
    left: 300px; top: 55px;
    width: 600px; height: 850px;
    background: var(--paper);
    overflow: hidden;
    box-shadow: 0 8px 24px rgba(0,0,0,.18);
  }
  .hero-photo {
    position: absolute; left: 0; top: 0;
    width: 600px; height: 380px;
    background: linear-gradient(120deg, #8a8580 0%, #c9bfb4 38%, #e9e5e0 62%, #4d4d4f 100%);
  }
  .shapes { position: absolute; left: 0; top: 0; width: 600px; height: 850px; }
  .tagline {
    position: absolute; left: 38px; top: 262px;
    color: #fff; font-size: 19px; font-weight: 400; line-height: 1.3;
  }
  .tagline .accent { color: var(--blue-light); font-weight: 700; font-size: 22px; }
  .brand-name {
    position: absolute; left: 462px; top: 350px;
    color: #fff; font-size: 24px; font-weight: 600; white-space: nowrap;
  }
  .offer-title {
    position: absolute; left: 32px; top: 372px;
    color: var(--green); font-size: 31px; font-weight: 800;
  }
  .offer-note {
    position: absolute; left: 32px; top: 413px;
    color: var(--green); font-size: 18px; font-weight: 600;
  }
  .offer-box {
    position: absolute; left: 30px; top: 446px; width: 545px;
    background: var(--blue); color: #fff;
    font-size: 12.5px; line-height: 1.45; padding: 8px 14px;
  }
  .independent-icon { position: absolute; left: 32px; top: 516px; }
  .independent-title {
    position: absolute; left: 82px; top: 518px; width: 500px;
    font-size: 18px; line-height: 1.2; color: var(--grey-text); font-weight: 800;
  }
  .independent-title .note { color: var(--green); font-weight: 600; font-size: 17px; }
  .independent-body {
    position: absolute; left: 32px; top: 572px; width: 540px;
    font-size: 11.5px; line-height: 1.45; color: var(--dark-text);
  }
  .call-title {
    position: absolute; left: 32px; top: 632px; width: 560px;
    font-size: 18px; color: var(--dark-text); font-weight: 800; white-space: nowrap;
  }
  .call-title .note { color: var(--green); font-weight: 600; font-size: 15px; }
  .locations { position: absolute; left: 32px; top: 668px; list-style: none; }
  .location { display: flex; align-items: baseline; gap: 8px; margin-bottom: 6px; }
  .location .suburb { width: 62px; color: var(--green); font-size: 13px; font-weight: 600; }
  .location .phone { color: var(--grey-text); font-size: 16px; font-weight: 700; }
  .location .address { color: var(--green); font-size: 13px; }
  .supplier-band {
    position: absolute; left: 0; top: 770px; width: 600px; height: 80px;
    background: var(--band);
  }
  .supplier-label {
    position: absolute; left: 32px; top: 30px;
    color: var(--blue); font-size: 12px; font-weight: 600;
  }
  .supplier { position: absolute; font-size: 13px; font-weight: 700; white-space: nowrap; }
  .supplier.brandle { left: 140px; top: 20px; color: var(--navy); }
  .supplier.vordane { left: 255px; top: 36px; color: var(--grey-text); }
  .supplier.kylofen { left: 370px; top: 52px; color: var(--navy); }
  .machine-photo {
    position: absolute; left: 425px; top: 700px;
    width: 140px; height: 140px; border-radius: 50%;
    border: 5px solid var(--blue);
    background: radial-gradient(circle at 50% 50%, #3a3a3c 0%, #6a6a6e 38%, #e3e6ea 62%, #ffffff 100%);
  }
</style>
</head>
<body>
  <article class="flyer">
    <div class="hero-photo" role="img" aria-label="Photo of a man sleeping comfortably wearing a CPAP nasal mask beside a CPAP machine"></div>

    <svg class="shapes" viewBox="0 0 600 850" aria-hidden="true">
      <defs>
        <clipPath id="below-swoosh">
          <path d="M0 372 C240 372 480 320 600 205 L600 850 L0 850 Z"/>
        </clipPath>
      </defs>
      <path d="M0 372 C240 372 480 320 600 205 L600 850 L0 850 Z" fill="var(--paper)"/>
      <circle cx="640" cy="240" r="230" fill="var(--green)" clip-path="url(#below-swoosh)"/>
      <path d="M0 355 C230 360 470 300 600 165 L600 205 C480 320 240 372 0 372 Z" fill="var(--blue-light)"/>
      <path d="M0 330 C220 350 460 280 600 110 L600 165 C470 300 230 360 0 355 Z" fill="var(--blue)"/>
    </svg>

    <p class="tagline">Helping You Sleep<br><span class="accent">Right and Live</span> Better</p>

    <p class="brand-name">CPAP NEST</p>

    <h1 class="offer-title">$99 CPAP TRIAL</h1>
    <p class="offer-note">(prominent - this is the main point of the flyer)</p>
    <p class="offer-box">Our all inclusive 4 week CPAP or APAP trial includes everything you need to get started for just $99. Plus we'll refund your trial fee when you're ready to buy your own machine.</p>

    <svg class="independent-icon" width="40" height="34" viewBox="0 0 40 34" aria-hidden="true">
      <path d="M18 32 C6 22 0 16 0 9 C0 4 4 0 9 0 C13 0 16 2 18 6 C20 2 23 0 27 0 C32 0 36 4 36 9 C36 16 30 22 18 32 Z" fill="var(--blue)"/>
      <circle cx="31" cy="25" r="8" fill="var(--paper)" stroke="var(--blue)" stroke-width="2"/>
      <path d="M31 20 V30 M26 25 H36" stroke="var(--blue)" stroke-width="2.5"/>
    </svg>
    <h2 class="independent-title">PROUDLY INDEPENDENT! <span class="note">(keep this separate from themain promotion)</span></h2>
    <p class="independent-body">Many CPAP clinics in Victoria are now owned by one or other of the big CPAP manufacturers; while many others only stock one brand. We stock all the leading brands and offer genuinely independent advice and friendly service.</p>

    <h2 class="call-title">CALL US FOR AN APPOINTMENT <span class="note">(suburb and phone prominent)</span></h2>
    <ul class="locations">
      <li class="location"><span class="suburb">Ashburton</span><span class="phone">(03) 5550 1842</span><span class="address">5/317 Lantern Street</span></li>
      <li class="location"><span class="suburb">Brighton</span><span class="phone">(03) 5550 2967</span><span class="address">27b Penrose Grove</span></li>
      <li class="location"><span class="suburb">Kew East</span><span class="phone">(03) 5550 3175</span><span class="address">2816 Tamsin Road</span></li>
    </ul>

    <footer class="supplier-band">
      <span class="supplier-label">SUPPLIER LOGOS</span>
      <span class="supplier brandle">Brandle&amp;Voss</span>
      <span class="supplier vordane">Vordane Restiva</span>
      <span class="supplier kylofen">Kylofen</span>
    </footer>

    <div class="machine-photo" role="img" aria-label="Photo of a Kylofen CPAP machine with humidifier"></div>
  </article>
</body>
</html>
```